Contractor Plan "B"/Getting Screwed?/Something Useful

We are sending out a series of postcards to a group of local contractors.

The first in the series is: Plan B: Pink Bubble Wrap. Plan A is to buy insurance from my agency. This will be printed, front and back on card stock. We will then glue a piece of bubble wrap to the card and place it in an envelope for delivery.

The second card will be along the same lines but will ask if the client is getting screwed by his current Insurance Company. We will glue a screw in the middle of the card and place the card in an envelope for delivery. On the bottom of we might tell them to call us to get unscrewed.

The third card will follow those lines but say something like: We sent you bubble wrap for your Plan B and you didn't call. Then we sent you something funny but you didn't call. We decided to send you something useful so you might call now! With this card, we are going to send a carpenter pencil.

I am attaching a rough outline of my sketch design for the first card so you will have basic information we will need such as phone number and coverages we offer. If you feel like there is too much info for the size of the card, we can leave some off. I just want the phone to ring! Also, feel free to adjust the wording to make it work better...creative design is not my strong suit!!

I would like for all three cards to be designed. Each can have the same backside. Also, please keep in mind, this is not a postcard so you don't have to leave the blanks on the back for addressing. Each will be mailed in an envelope.

I have also uploaded my logo file as we have recently redone the logo.

Here is more guidance on the project: The cards are going to be 10 cm wide and 23 cm tall. I have added more wording in the brief. Also, I attached a word doc with a good idea of what to use for wording. Basically I want the following idea: Card 1: At top of card - Plan B: Pink Bubble Wrap Below the bubble wrap - Plan A: Call us so you don't have to use Pink Bubble Wrap Card 2: At top of card - Getting Screwed? Is your current agent taking you for granted? Below the area where we are going to glue a screw - Get unscrewed, Call us! Card 3: At top of card - We have the sharpest pencil in town! We will leave space for a carpenter pencil to be attached tot he card. On the other side of the open space - Call us today for the best rates on your insurance!

Please review the attached word doc for an idea of what to put on the back of the card. To be clear, we need three designs for the front of the card and can probably use just one design for the back of all three. If you think we need to have a different design for the back of each, I would like to see your ideas. Thank you for your hard work on these!

Reason: Hi, I am extending the time as I am expecting a few more submissions. Thank you!

Target Market(s)

We are targeting both contractors and truckers with this campaign.

Industry/Entity Type

Insurance

Requirements
Must have
• Clever wording. It needs to be a call to action and doesn't need to have too many specifics.

We also have to have space in the middle to glue the bubble wrap on the first card, the screw in the second and attach the pencil in the third.

```html
<!DOCTYPE html>
<html lang="en">
<head>
<meta charset="utf-8">
<title>Getting Screwed? – Harbor Line Insurance</title>
<link rel="stylesheet" href="https://fonts.googleapis.com/css2?family=Inter:wght@300;800&display=swap">
<style>
  :root {
    --cyan: #20e6ef;
    --cyan-deep: #14cfd9;
    --white: #ffffff;
  }
  html, body {
    margin: 0;
    padding: 0;
    width: 1200px;
    height: 2755px;
    overflow: hidden;
    background: var(--cyan);
  }
  .card {
    position: relative;
    width: 1200px;
    height: 2755px;
    overflow: hidden;
    font-family: "Inter", Arial, sans-serif;
    color: var(--white);
    text-align: center;
  }
  .texture {
    position: absolute;
    inset: 0;
    background: radial-gradient(ellipse at center, #25e9f2 0%, var(--cyan) 60%, #1bdde7 100%);
  }
  .foot-band {
    position: absolute;
    left: 0;
    right: 0;
    bottom: 0;
    height: 48px;
    background: var(--cyan-deep);
  }
  .headline {
    position: absolute;
    top: 118px;
    left: 0;
    right: 0;
    margin: 0;
    font-weight: 800;
    font-size: 168px;
    line-height: 0.95;
    letter-spacing: -2px;
  }
  .subhead {
    position: absolute;
    top: 500px;
    left: 0;
    right: 0;
    margin: 0;
    font-weight: 300;
    font-size: 78px;
    line-height: 1.12;
    letter-spacing: -1px;
  }
  .screw-spot {
    position: absolute;
    top: 1254px;
    left: 532px;
    width: 136px;
    height: 136px;
  }
  .cta {
    position: absolute;
    top: 1530px;
    left: 0;
    right: 0;
    margin: 0;
    font-weight: 300;
    font-size: 80px;
    letter-spacing: -1px;
  }
  .phone {
    position: absolute;
    top: 1680px;
    left: 0;
    right: 0;
    margin: 0;
    font-weight: 800;
    font-size: 132px;
    letter-spacing: -2px;
  }
  .brand {
    position: absolute;
    top: 2340px;
    left: 0;
    right: 0;
    margin: 0;
    font-weight: 800;
    font-size: 112px;
    line-height: 1;
    letter-spacing: -1px;
  }
  .brand span {
    display: block;
    font-size: 56px;
    margin-top: 18px;
    letter-spacing: 2px;
  }
</style>
</head>
<body>
  <div class="card">
    <div class="texture" role="img" aria-label="Repeating pattern of small cyan screw heads covering the card"></div>
    <div class="foot-band"></div>

    <h1 class="headline">GETTING<br>SCREWED?</h1>
    <p class="subhead">Is your current agent<br>taking you for granted?</p>

    <svg class="screw-spot" viewBox="0 0 136 136" aria-hidden="true">
      <circle cx="68" cy="68" r="66" fill="#ffffff"/>
      <path d="M46 46 L90 90 M90 46 L46 90" stroke="#20e6ef" stroke-width="18" stroke-linecap="round"/>
    </svg>

    <p class="cta">Call us to get unscrewed!</p>
    <p class="phone">555-014-2273</p>

    <p class="brand">HARBOR LINE<span>INSURANCE</span></p>
  </div>
</body>
</html>
```